New Alcoholic Spiked Seltzer Line

We need a can design for a line of low calorie alcoholic seltzer. This product is a sparkling water and vodka drink with no sugar added in a slim 12 oz can.

This is a lighter, healthier, alternative to the sugary ready-to-drinks on the market. The product contains only 3 ingredients: Vodka, Water and Natural Flavors. It has only 100 calories but still has 5% alcohol, so you don't need to sacrifice alcohol to cut calories.

This product also does not contain any preservatives.

We want this design to communicate the following objectives to the consumer and in this order:

1. Appetizing product
2.Low calorie
3.Communicate the type of beverage (Spiked Seltzer)

The brand name of the product is VELKA.

The flavor of the product needed to be used for the design is Mango-Orange.

Comparable products are:

www.brisavelfizz.example/
https://www.tarnowbubble.example
https://quellrind.example/

The designs should not infringe or copy the creative directions of the products mentionned above. They are only given so that you can better understand the type of product we are developing.

Target Market(s)

Young Professional women between the ages of 25 and 44

Industry/Entity Type

Product

Colors

Designer to choose colors to be used in the design.

Requirements
Must have
• Design extendibility, meaning it can be adapted for other flavors.
• This is a new category in the market we are targeting, so consumers must easily be able to identify what type of product this is.

```html
<!DOCTYPE html>
<html lang="en">
<head>
<meta charset="utf-8">
<title>VELKA Spiked Seltzer – Mango-Orange Can Label</title>
<link rel="stylesheet" href="https://fonts.googleapis.com/css2?family=Fredoka:wght@500;700&family=Montserrat:wght@600;700&display=swap">
<style>
  :root {
    --stage: #e9edf0;
    --label-white: #fbfcfd;
    --mango: #f6a223;
    --mango-deep: #ef8f17;
    --sky: #29a3d9;
    --lime: #6cb844;
    --dot-blue: #1f63b5;
    --dot-cyan: #2bc3e8;
    --dot-green: #7cc242;
    --dot-yellow: #f3d233;
    --ink-white: #ffffff;
  }
  html, body {
    margin: 0;
    width: 1200px;
    height: 674px;
    overflow: hidden;
    background: var(--stage);
  }
  .canvas {
    position: relative;
    width: 1200px;
    height: 674px;
  }
  .can-label {
    position: absolute;
    left: 340px;
    top: 20px;
    width: 520px;
    height: 634px;
  }
  .brand-name {
    font-family: "Fredoka", sans-serif;
    font-weight: 700;
    font-size: 104px;
    fill: var(--ink-white);
    letter-spacing: 2px;
  }
  .product-type {
    font-family: "Montserrat", sans-serif;
    font-weight: 700;
    font-size: 21px;
    letter-spacing: 7px;
    fill: var(--ink-white);
  }
  .badge-text {
    font-family: "Fredoka", sans-serif;
    font-weight: 500;
    fill: var(--ink-white);
  }
  .badge-text--low { font-size: 17px; }
  .badge-text--no-big { font-size: 34px; font-weight: 700; }
  .badge-text--no-small { font-size: 11px; }
  .flavor-name {
    font-family: "Montserrat", sans-serif;
    font-weight: 700;
    font-size: 19px;
    letter-spacing: 1px;
    fill: var(--mango-deep);
  }
</style>
</head>
<body>
<main class="canvas">
  <svg class="can-label" viewBox="0 0 520 634" xmlns="http://www.w3.org/2000/svg">
    <defs>
      <linearGradient id="bubble-field-top" x1="0" y1="0" x2="0" y2="1">
        <stop offset="0" stop-color="var(--dot-blue)" stop-opacity="0.55"/>
        <stop offset="0.6" stop-color="var(--dot-cyan)" stop-opacity="0.35"/>
        <stop offset="1" stop-color="var(--dot-cyan)" stop-opacity="0"/>
      </linearGradient>
      <linearGradient id="bubble-field-sides" x1="0" y1="0" x2="0" y2="1">
        <stop offset="0" stop-color="var(--dot-cyan)" stop-opacity="0.3"/>
        <stop offset="0.5" stop-color="var(--dot-green)" stop-opacity="0.35"/>
        <stop offset="1" stop-color="var(--dot-yellow)" stop-opacity="0.35"/>
      </linearGradient>
    </defs>

    <rect class="label-base" x="0" y="0" width="520" height="634" fill="var(--label-white)"/>

    <g class="bubble-pattern" role="img" aria-label="Rising bubble dot pattern in blue, cyan, green and yellow">
      <path d="M0 0 H520 V230 Q260 120 0 230 Z" fill="url(#bubble-field-top)"/>
      <rect x="0" y="150" width="40" height="420" fill="url(#bubble-field-sides)"/>
      <rect x="480" y="150" width="40" height="420" fill="url(#bubble-field-sides)"/>
    </g>

    <circle class="flavor-disc" cx="262" cy="370" r="188" fill="var(--mango)"/>

    <text class="brand-name" x="262" y="408" text-anchor="middle">VELKA</text>
    <text class="product-type" x="262" y="470" text-anchor="middle">SPIKED SELTZER</text>

    <g class="badge badge--low-calorie">
      <circle cx="72" cy="236" r="50" fill="var(--sky)"/>
      <text class="badge-text badge-text--low" x="72" y="232" text-anchor="middle">LOW</text>
      <text class="badge-text badge-text--low" x="72" y="254" text-anchor="middle">CALORIE</text>
    </g>

    <g class="badge badge--no-sugar">
      <circle cx="448" cy="556" r="54" fill="var(--lime)"/>
      <text class="badge-text badge-text--no-big" x="438" y="570" text-anchor="middle">NO</text>
      <text class="badge-text badge-text--no-small" x="482" y="553" text-anchor="middle">SUGAR</text>
      <text class="badge-text badge-text--no-small" x="482" y="567" text-anchor="middle">ADDED</text>
    </g>

    <text class="flavor-name" x="262" y="612" text-anchor="middle">MANGO–ORANGE</text>
  </svg>
</main>
</body>
</html>
```